Letterhead Design Project

Sunmark Growth Coaching Services

My info is
Daryna Feltwick-Osbourne
daryna@sunmarkgrowthco.com
sunmarkgrowthco.com
555-314-7720

you can play with order of items. I've never had a letterhead before. Thank you!

```html
<!DOCTYPE html>
<html lang="en">
<head>
<meta charset="UTF-8">
<title>Sunmark Growth Coaching Services – Letterhead</title>
<link rel="stylesheet" href="https://fonts.googleapis.com/css2?family=Arimo:wght@400;700&display=swap">
<style>
  :root {
    --brand-orange: #f7941d;
    --brand-red: #c0112f;
    --band-rule: #fbd3a3;
    --footer-grey: #c9c9c9;
    --paper: #ffffff;
  }
  html, body {
    margin: 0;
    padding: 0;
    overflow: hidden;
    background: var(--paper);
  }
  .letterhead {
    position: relative;
    width: 883px;
    height: 1200px;
    overflow: hidden;
    background: var(--paper);
    font-family: "Arimo", Arial, sans-serif;
  }
  .brand-mark {
    position: absolute;
    left: 200px;
    top: 6px;
    width: 210px;
    text-align: center;
  }
  .brand-mark__dot {
    display: block;
    margin: 0 auto 8px;
  }
  .brand-mark__name {
    margin: 0;
    color: var(--brand-red);
    font-weight: 700;
    font-size: 16px;
    line-height: 20px;
    letter-spacing: 0.5px;
  }
  .contact {
    position: absolute;
    left: 535px;
    top: 44px;
    margin: 0;
    padding: 0;
    list-style: none;
    color: var(--brand-red);
    font-size: 17px;
    line-height: 21.5px;
  }
  .title-band {
    position: absolute;
    left: 0;
    top: 152px;
    width: 883px;
    height: 49px;
    background: var(--brand-orange);
  }
  .title-band__rule {
    position: absolute;
    top: 0;
    width: 1px;
    height: 49px;
    background: var(--band-rule);
  }
  .title-band__rule--left { left: 126px; }
  .title-band__rule--right { left: 718px; }
  .title-band__text {
    margin: 0;
    text-align: center;
    color: var(--paper);
    font-weight: 700;
    font-size: 29px;
    line-height: 49px;
    padding-left: 0;
    width: 883px;
    transform: translateX(-3px);
  }
  .footer-mark {
    position: absolute;
    left: 0;
    top: 1086px;
    width: 883px;
    text-align: center;
    opacity: 0.35;
  }
  .footer-mark__dot { display: block; margin: 0 auto 4px; }
  .footer-mark__name {
    margin: 0;
    color: var(--brand-red);
    font-weight: 700;
    font-size: 9px;
    line-height: 11px;
  }
  .footer-title {
    position: absolute;
    left: 0;
    top: 1158px;
    width: 883px;
    margin: 0;
    text-align: center;
    color: var(--footer-grey);
    font-weight: 700;
    font-size: 31px;
    line-height: 40px;
  }
</style>
</head>
<body>
  <div class="letterhead">
    <div class="brand-mark">
      <svg class="brand-mark__dot" width="72" height="72" viewBox="0 0 72 72" aria-hidden="true">
        <circle cx="36" cy="36" r="34" fill="var(--brand-orange)"/>
      </svg>
      <p class="brand-mark__name">Sunmark Growth<br>Coaching Services</p>
    </div>

    <ul class="contact">
      <li>Daryna Feltwick-Osbourne</li>
      <li>555-314-7720</li>
      <li>daryna@sunmarkgrowthco.com</li>
      <li>sunmarkgrowthco.com</li>
    </ul>

    <div class="title-band">
      <span class="title-band__rule title-band__rule--left"></span>
      <span class="title-band__rule title-band__rule--right"></span>
      <h1 class="title-band__text">Sunmark Growth Coaching Services</h1>
    </div>

    <div class="footer-mark">
      <svg class="footer-mark__dot" width="30" height="30" viewBox="0 0 30 30" aria-hidden="true">
        <circle cx="15" cy="15" r="14" fill="var(--brand-orange)"/>
      </svg>
      <p class="footer-mark__name">Sunmark Growth</p>
    </div>

    <p class="footer-title">Sunmark Growth Coaching Services</p>
  </div>
</body>
</html>
```